Visitenkarten-Design für Lichtfeder - Zeilen von Hand zu Hand
Zielgruppe
Ich schreibe Briefe an Menschen, die mehr über sich erfahren wollen, die sich berühren lassen wollen, die an sich arbeiten möchten, die sich entfalten wollen. Ich möchte nicht den Verstand sondern das Herz ansprechen, die Selbstheilung erfahren möchten, damit sie Impulse bekommen, um ein glücklicheres Leben zu führen, das ihnen mehr entspricht.
Ich sehe mich als Mensch, der andere Menschen in ihrem Leben unterstützen möchte.
Aufgabenstellung
Die Briefe schreibe ich in Segoe Print, goldene Schrift auf gelblichem Papier, evtl auch anderes Papier, wenn die goldene Schrift passt.
Die Visitenkarte sollte Freude, Freiheit und Anerkennung des Menschen an sich ausstrahlen. Farben evtl. Bordeaux, mit vielleicht Rosa. Sie sollte jedoch nicht kitschig wirken.
Schön wäre vielleicht etwas mit Blumen oder Ornamenten, jedoch nicht zu überladen.
Als Text soll drauf sein:
Das beigefügte Logo, dann:
Berühren - Bewegen - Begeistern

```html
<!DOCTYPE html>
<html lang="de">
<head>
<meta charset="utf-8">
<title>Lichtfeder – Visitenkarte</title>
<link rel="stylesheet" href="https://fonts.googleapis.com/css2?family=Kalam:wght@400&family=Open+Sans:wght@400;700&display=swap">
<style>
  :root {
    --bordeaux: #6b1730;
    --bordeaux-light: #8c1f40;
    --gold: #d4b04a;
    --gold-dark: #9a6a1e;
    --rose: #de86b0;
    --white: #ffffff;
    --backdrop: #dfe3e6;
  }
  * { margin: 0; padding: 0; box-sizing: border-box; }
  html, body { width: 1200px; height: 900px; overflow: hidden; }
  body { background: var(--backdrop); position: relative; font-family: "Open Sans", sans-serif; }

  .card { position: absolute; width: 560px; height: 340px; overflow: hidden; box-shadow: 0 6px 18px rgba(0,0,0,.18); }

  /* Back side */
  .card-back { left: 60px; top: 80px; background: var(--bordeaux); }
  .card-back .brand-mark {
    position: absolute; left: 50px; top: 130px;
    display: flex; align-items: center; gap: 14px;
    font-family: "Kalam", cursive; font-weight: 400; font-size: 52px; color: var(--gold);
  }
  .card-back .brand-dot { width: 22px; height: 22px; border-radius: 50%; background: var(--bordeaux-light); }
  .motto { position: absolute; left: 330px; top: 70px; list-style: none;
    font-family: "Kalam", cursive; font-size: 32px; color: var(--white); line-height: 1.6; }
  .motto li:nth-child(2) { padding-left: 30px; }
  .motto li:nth-child(3) { padding-left: 50px; }

  /* Front side */
  .card-front { left: 580px; top: 480px; background: var(--white); }
  .card-front .waves { position: absolute; inset: 0; }
  .logo { position: absolute; left: 56px; top: 34px; }
  .logo-name { font-family: "Kalam", cursive; font-weight: 400; font-size: 64px; line-height: 1; color: var(--bordeaux); }
  .logo-tagline { margin-top: 4px; padding-left: 90px; font-size: 12px; letter-spacing: 2px; text-transform: uppercase; color: var(--bordeaux-light); }
  .person-name { position: absolute; left: 60px; top: 156px; font-weight: 700; font-size: 22px; color: var(--bordeaux); }
  .contact { position: absolute; color: var(--white); font-size: 14px; display: flex; align-items: center; gap: 8px; }
  .contact svg { width: 16px; height: 16px; flex: none; }
  .contact-mail { left: 350px; top: 224px; }
  .contact-phone { left: 350px; top: 250px; }
  .contact-web { left: 60px; top: 300px; }
</style>
</head>
<body>

<section class="card card-back" aria-label="Kartenrückseite">
  <div class="brand-mark"><span class="brand-dot"></span>Lichtfeder</div>
  <ul class="motto">
    <li>Berühren</li>
    <li>Bewegen</li>
    <li>Begeistern</li>
  </ul>
</section>

<section class="card card-front" aria-label="Kartenvorderseite">
  <svg class="waves" viewBox="0 0 560 340" preserveAspectRatio="none" aria-hidden="true">
    <defs>
      <linearGradient id="goldBand" x1="0" y1="1" x2="1" y2="0">
        <stop offset="0" stop-color="#9a6a1e"/>
        <stop offset="1" stop-color="#d4b04a"/>
      </linearGradient>
    </defs>
    <path class="rose-stripe" d="M0 226 C170 222 330 195 420 140 C360 200 200 237 0 240 Z" fill="var(--rose)"/>
    <path class="gold-band" d="M0 248 C230 244 440 205 560 15 L560 340 L0 340 Z" fill="url(#goldBand)"/>
    <path class="bordeaux-field" d="M0 260 C240 256 450 220 560 40 L560 340 L0 340 Z" fill="var(--bordeaux)"/>
  </svg>

  <div class="logo">
    <div class="logo-name">Lichtfeder</div>
    <div class="logo-tagline">Zeilen von Hand zu Hand</div>
  </div>

  <div class="person-name">Marlene Hofbauer</div>

  <div class="contact contact-mail">
    <svg viewBox="0 0 16 16"><rect x="1" y="3" width="14" height="10" fill="var(--gold)"/><path d="M1 3 L8 9 L15 3" fill="none" stroke="var(--bordeaux)" stroke-width="1.2"/></svg>
    lichtfeder@post-mail.de
  </div>
  <div class="contact contact-phone">
    <svg viewBox="0 0 16 16"><path d="M4 1 L6.5 4.5 L5 6 C6 8.5 7.5 10 10 11 L11.5 9.5 L15 12 L13 15 C7 14.5 1.5 9 1 3 Z" fill="var(--gold)"/></svg>
    +49 151 23 456 789
  </div>
  <div class="contact contact-web">
    <svg viewBox="0 0 16 16"><circle cx="8" cy="8" r="7" fill="var(--gold)"/><path d="M1 8 H15 M8 1 C5 4 5 12 8 15 M8 1 C11 4 11 12 8 15" fill="none" stroke="var(--bordeaux)" stroke-width="1"/></svg>
    www.marlenehofbauer.de
  </div>
</section>

</body>
</html>
```